Medtech Advisory- Brixholm Equity Associates Website

We need a company website, programmed in Typo3.
The design should be clean, modern and simple based on the color and style of our logo.
Brixholm Equity Associates is a Swiss company which assists international medtech companies in relocating all or part of their business to Switzerland.
The site should consist of the following pages: Home, Offering, Customers, Team, Contact us (see also attached pdf file).
Target Market(s)
Medtech Start-ups
Industry/Entity Type
It Company
Coding
Coded - Design and coding required
Requirements
Must have
- Use of the logo provided
- page structure as described above
- programmed in Typo3 so that we can edit ourselves
- responsive for use with mobile devices
Nice to have
- eye catcher to attract readers interest, e.g. visuals

```html
<!DOCTYPE html>
<html lang="en">
<head>
<meta charset="utf-8">
<title>Brixholm Equity Associates – Medtech Advisory</title>
<link rel="stylesheet" href="https://fonts.googleapis.com/css2?family=Barlow:wght@300;400;500&family=Open+Sans:wght@400;600;700&display=swap">
<style>
:root{
  --blue:#2f6fb5;
  --blue-head:#3b77bb;
  --blue-dark:#2a62a3;
  --blue-footer:#3877b9;
  --blue-bottom:#2d66a6;
  --text:#8a8a8a;
  --text-dark:#555;
  --light:#f5f5f5;
  --line:#c9c9c9;
  --red:#d7261e;
  --white:#fff;
}
*{margin:0;padding:0;box-sizing:border-box}
html,body{width:1200px;height:3000px;overflow:hidden;background:var(--white)}
body{position:relative;font-family:"Open Sans",Arial,sans-serif;color:var(--text)}
.abs{position:absolute}
.heading{font-family:"Barlow",Arial,sans-serif;font-weight:300;color:var(--blue-head);font-size:34px;letter-spacing:1px;text-transform:uppercase}
.rule{position:absolute;height:2px;width:66px;background:var(--line)}

/* top bar */
.topbar-call{left:90px;top:14px;font-size:14px;color:#999}
.topbar-call span{color:var(--blue)}
.social-dot{width:16px;height:16px;border-radius:50%;background:#c4c4c4;top:14px}
.contact-btn{left:976px;top:0;width:134px;height:42px;background:var(--blue);color:#fff;font-size:14px;display:flex;align-items:center;justify-content:center}

/* nav */
.brand{left:88px;top:62px;display:flex;align-items:center;gap:10px;font-family:"Barlow",sans-serif;font-weight:500;font-size:30px;color:var(--blue)}
.brand i{width:26px;height:26px;border-radius:50%;background:var(--blue);display:block}
.nav{top:72px;font-size:14px;color:#666}
.nav.active{color:var(--blue);font-weight:700}

/* hero */
.hero{left:0;top:126px;width:1200px;height:504px;background:linear-gradient(100deg,#e7f1f8 0%,#d6e8f4 45%,#eef3f6 75%,#e9d8d4 100%)}
.hero-box{left:314px;top:260px;width:568px;height:166px;background:rgba(47,111,181,.88);padding:8px}
.hero-box-inner{width:100%;height:100%;border:2px dashed rgba(255,255,255,.8);text-align:center;color:#fff;font-family:"Barlow",sans-serif}
.hero-line1{font-size:26px;font-weight:500;margin-top:22px}
.hero-line2{font-size:50px;font-weight:400;letter-spacing:2px;margin-top:6px}

/* who we are */
.who-text{left:90px;top:780px;width:520px;font-size:15px;line-height:28px}
.photo{background:linear-gradient(135deg,#cfc3b3,#b69d7c 55%,#8a7763)}

/* why switzerland */
.why-bg{left:600px;top:1040px;width:600px;height:440px;background:var(--light)}
.why-list{left:636px;top:1162px;list-style:none;font-size:14px;letter-spacing:.5px}
.why-list li{height:34px;display:flex;align-items:center;gap:12px}
.why-list svg{flex:none}

/* industry */
.center{left:0;width:1200px;text-align:center}
.pill{left:216px;top:1640px;width:768px;height:352px;border-radius:176px;background:#eeeeee;border:2px solid #e2e2e2}
.map{left:290px;top:1644px;width:620px;height:344px;background:var(--red)}
.chain-label{left:0;width:1200px;top:1746px;text-align:center;color:#fff;font-weight:700;font-size:24px}
.chain{left:286px;top:1790px;width:620px;height:42px;border-radius:21px;background:var(--blue);display:flex;align-items:center;justify-content:center;gap:14px;color:#fff;font-size:18px}
.stat{width:132px;height:132px;border-radius:50%;background:var(--blue);border:6px solid #fff;box-shadow:0 0 0 2px #e3e3e3,0 4px 8px rgba(0,0,0,.2);display:flex;align-items:center;justify-content:center;text-align:center;color:#fff;font-weight:700;font-size:17px;line-height:22px}

/* team */
.card{top:2142px;width:206px;height:318px;background:var(--light);text-align:center;padding:8px}
.card-photo{width:190px;height:194px}
.card-name{margin-top:16px;font-size:16px;color:var(--text-dark);letter-spacing:.5px}
.card-rule{width:22px;height:3px;background:var(--blue);margin:10px auto 10px}
.card-desc{font-size:14px;line-height:22px;padding:0 8px;height:44px;overflow:hidden}

/* footer */
.footer{left:0;top:2530px;width:1200px;height:470px;background:var(--blue-footer);color:#fff}
.footer-brand{top:40px;left:0;width:1200px;text-align:center;font-family:"Barlow",sans-serif;font-weight:500;font-size:34px}
.news{top:110px;left:0;width:1200px;text-align:center;font-family:"Barlow",sans-serif;font-size:30px;letter-spacing:1px}
.email{left:362px;top:162px;width:342px;height:38px;background:var(--blue-dark);font-size:12px;color:#8fb3dc;padding:11px 14px}
.subscribe{left:706px;top:162px;width:132px;height:38px;background:#fff;color:var(--blue);font-size:13px;display:flex;align-items:center;justify-content:center;letter-spacing:.5px}
.divider{left:0;top:244px;width:1200px;height:1px;background:rgba(255,255,255,.2)}
.col-title{top:276px;font-size:15px;font-weight:600}
.col-links{top:304px;font-size:13px;line-height:21px;color:#c9dcf1}
.round{width:30px;height:30px;border-radius:50%;border:2px solid #fff;top:304px}
.footer-phone{left:960px;top:352px;font-size:18px;color:#c9dcf1;letter-spacing:1px}
.bottom{left:0;top:420px;width:1200px;height:50px;background:var(--blue-bottom);text-align:center;font-size:12px;line-height:50px;color:#c9dcf1}
</style>
</head>
<body>

<!-- top bar -->
<div class="abs topbar-call">Call Us: <span>123-456-7890</span></div>
<div class="abs social-dot" style="left:836px"></div>
<div class="abs social-dot" style="left:884px"></div>
<div class="abs social-dot" style="left:934px"></div>
<div class="abs contact-btn">CONTACT US</div>

<!-- header -->
<div class="abs brand"><i></i>Brixholm</div>
<div class="abs nav active" style="left:568px">Home</div>
<div class="abs nav" style="left:676px">What we do</div>
<div class="abs nav" style="left:818px">Services</div>
<div class="abs nav" style="left:938px">Customers</div>
<div class="abs nav" style="left:1074px">Team</div>

<!-- hero -->
<div class="abs hero" role="img" aria-label="Doctor's hand holding a stethoscope beside floating medical icons on a light blue background"></div>
<div class="abs hero-box">
  <div class="hero-box-inner">
    <div class="hero-line1">Brixholm Equity Associates is helping in the</div>
    <div class="hero-line2">MEDTECH SECTOR</div>
  </div>
</div>

<!-- who we are -->
<div class="abs heading" style="left:90px;top:688px">Who we are</div>
<div class="rule" style="left:90px;top:752px"></div>
<p class="abs who-text">Brixholm Equity Associates is a Swiss company helping startups in the medtech sector establish themselves in Switzerland.<br>Our Mission is to help startup companies maximize their potential in an ideal environment</p>
<div class="abs photo" style="left:672px;top:694px;width:438px;height:278px" role="img" aria-label="Team of young people with moving boxes holding start-up signs"></div>

<!-- why switzerland -->
<div class="abs photo" style="left:0;top:1040px;width:600px;height:440px;background:linear-gradient(135deg,#efe6d8,#d8c3a4 50%,#a98f6e)" role="img" aria-label="Woman on the phone at an office desk with passports and a Swiss flag"></div>
<div class="abs why-bg"></div>
<div class="abs heading" style="left:636px;top:1070px">Why Switzerland</div>
<div class="rule" style="left:636px;top:1134px"></div>
<ul class="abs why-list">
  <li><svg width="14" height="12" viewBox="0 0 14 12"><path d="M1 6l4 4 8-9" fill="none" stroke="#b5b5b5" stroke-width="2.4"/></svg>Entrepreneurial environment</li>
  <li><svg width="14" height="12" viewBox="0 0 14 12"><path d="M1 6l4 4 8-9" fill="none" stroke="#b5b5b5" stroke-width="2.4"/></svg>Investment friendliness</li>
  <li><svg width="14" height="12" viewBox="0 0 14 12"><path d="M1 6l4 4 8-9" fill="none" stroke="#b5b5b5" stroke-width="2.4"/></svg>Uncomplicated tax system, low tax rates</li>
  <li><svg width="14" height="12" viewBox="0 0 14 12"><path d="M1 6l4 4 8-9" fill="none" stroke="#b5b5b5" stroke-width="2.4"/></svg>Specialized workforce</li>
  <li><svg width="14" height="12" viewBox="0 0 14 12"><path d="M1 6l4 4 8-9" fill="none" stroke="#b5b5b5" stroke-width="2.4"/></svg>Large medtech and life sciences industries</li>
  <li><svg width="14" height="12" viewBox="0 0 14 12"><path d="M1 6l4 4 8-9" fill="none" stroke="#b5b5b5" stroke-width="2.4"/></svg>Varied investors</li>
  <li><svg width="14" height="12" viewBox="0 0 14 12"><path d="M1 6l4 4 8-9" fill="none" stroke="#b5b5b5" stroke-width="2.4"/></svg>Universities and experts with international recognition</li>
  <li><svg width="14" height="12" viewBox="0 0 14 12"><path d="M1 6l4 4 8-9" fill="none" stroke="#b5b5b5" stroke-width="2.4"/></svg>Political and economical stability</li>
  <li><svg width="14" height="12" viewBox="0 0 14 12"><path d="M1 6l4 4 8-9" fill="none" stroke="#b5b5b5" stroke-width="2.4"/></svg>Quality of life</li>
</ul>

<!-- swiss medtech industry -->
<div class="abs heading center" style="top:1536px">Swiss Medtech Industry</div>
<div class="rule" style="left:567px;top:1602px"></div>
<div class="abs pill"></div>
<div class="abs map" role="img" aria-label="Red map of Switzerland with a white cross"></div>
<div class="abs chain-label">SMTI VALUE CHAIN</div>
<div class="abs chain">
  <span>Suppliers</span><span>›</span><span>Manufactures</span><span>›</span><span>Distributors</span><span>›</span><span>Services providers</span>
</div>
<div class="abs stat" style="left:98px;top:1652px">1,350<br>COMPANIES</div>
<div class="abs stat" style="left:98px;top:1852px">CHF 14.1<br>BILLION IN<br>SALES</div>
<div class="abs stat" style="left:970px;top:1652px">54,500<br>EMPLOYEES</div>
<div class="abs stat" style="left:970px;top:1852px">CHF 10.6<br>BILLION IN<br>EXPORTS</div>

<!-- our team -->
<div class="abs heading center" style="top:2042px">Our Team</div>
<div class="rule" style="left:567px;top:2108px"></div>
<div class="abs card" style="left:90px">
  <div class="card-photo photo" role="img" aria-label="Portrait of team member"></div>
  <div class="card-name">MATEO LINDQVIST</div><div class="card-rule"></div>
  <div class="card-desc">Mateo Lindqvist is a consultant for strategy development,</div>
</div>
<div class="abs card" style="left:362px">
  <div class="card-photo photo" role="img" aria-label="Portrait of team member"></div>
  <div class="card-name">SOPHIE MARCHAND</div><div class="card-rule"></div>
  <div class="card-desc">Sophie Marchand has a 25 years of business ...</div>
</div>
<div class="abs card" style="left:634px">
  <div class="card-photo photo" role="img" aria-label="Portrait of team member"></div>
  <div class="card-name">LENA ZURBRIGGEN</div><div class="card-rule"></div>
  <div class="card-desc">Lena Zurbriggen is co-founder of a boutique ...</div>
</div>
<div class="abs card" style="left:906px">
  <div class="card-photo photo" role="img" aria-label="Portrait of team member"></div>
  <div class="card-name">ANTON R. KELLER</div><div class="card-rule"></div>
  <div class="card-desc">Anton Keller has over 25 years of business ...</div>
</div>

<!-- footer -->
<footer class="abs footer">
  <div class="abs footer-brand">Brixholm</div>
  <div class="abs news">Subscribe to our Newsletter for latest news.</div>
  <div class="abs email">Your email</div>
  <div class="abs subscribe">SUBSCRIBE</div>
  <div class="abs divider"></div>

  <div class="abs col-title" style="left:90px">QUICK LINKS</div>
  <div class="abs col-links" style="left:90px">Home<br>Offering<br>Customers<br>Team<br>Contact us</div>

  <div class="abs col-title" style="left:530px">SERVICES</div>
  <div class="abs col-links" style="left:530px">Company set-up<br>Operational support<br>Medtech expertise</div>

  <div class="abs col-title" style="left:960px">CONNECT WITH US</div>
  <div class="abs round" style="left:960px"></div>
  <div class="abs round" style="left:1004px"></div>
  <div class="abs round" style="left:1048px"></div>
  <div class="abs footer-phone">123-456-7890</div>

  <div class="abs bottom">© 2016 Brixholm Equity Associates. All Rights Reserved.</div>
</footer>

</body>
</html>
```